Classy Home Bar menu in word format

The name of the bar is Bar Pemberly
8x10 bar menu black/gold lettering
classy coloring/font. Cover page for who we are. Next 9 pages will be drinks
drinks need to have a spot for names - brief description and a box for a picture
Drink menu should have a speakeasy vibe and be at least 10 pages long with different layouts

Target Market(s)

Visitors to our home. Friends family and guests

Industry/Entity Type

Bar guests

Font styles to use
Script

Requirements
Must have
• Class, easily editable, spots for pictures

```html
<!DOCTYPE html>
<html lang="en">
<head>
<meta charset="utf-8">
<title>Bar Pemberly – Menu Layouts</title>
<link rel="stylesheet" href="https://fonts.googleapis.com/css2?family=Great+Vibes&family=Monsieur+La+Doulaise&family=Berkshire+Swash&family=Cookie&family=Crimson+Pro:ital@1&display=swap">
<style>
  :root {
    --canvas: #ffffff;
    --charcoal: #2f2d2b;
    --ink: #000000;
    --gold-soft: #dcae6c;
    --gold-muted: #a8884e;
    --gold-bright: #efd163;
    --photo-cool: #1f3f7a;
    --photo-warm: #c7832f;
  }
  html, body { margin: 0; padding: 0; overflow: hidden; }
  body { width: 739px; height: 1200px; background: var(--canvas); position: relative; }
  .page { position: absolute; display: block; }
  .cover { left: 261px; top: 40px; width: 220px; height: 275px; }
  .col-1 { left: 44px; } .col-2 { left: 273px; } .col-3 { left: 500px; }
  .row-1 { top: 341px; } .row-2 { top: 627px; } .row-3 { top: 915px; }
  .page, .cover { width: 196px; height: 245px; }
  .cover { width: 220px; height: 275px; }
  .brand { font-family: 'Great Vibes', cursive; }
  .title-swash { font-family: 'Berkshire Swash', cursive; }
  .title-script { font-family: 'Monsieur La Doulaise', cursive; }
  .title-cookie { font-family: 'Cookie', cursive; }
  .desc { font-family: 'Crimson Pro', serif; font-style: italic; }
</style>
</head>
<body>

<svg width="0" height="0" style="position:absolute">
  <defs>
    <linearGradient id="photo-tone" x1="0" y1="0" x2="1" y2="1">
      <stop offset="0" stop-color="var(--photo-cool)"/>
      <stop offset="0.55" stop-color="#3b3a44"/>
      <stop offset="1" stop-color="var(--photo-warm)"/>
    </linearGradient>
  </defs>
</svg>

<!-- Cover -->
<svg class="page cover" viewBox="0 0 447 558">
  <rect width="447" height="558" fill="var(--charcoal)"/>
  <path d="M52 28 H395 A20 20 0 0 0 415 48 V510 A20 20 0 0 0 395 530 H52 A20 20 0 0 0 32 510 V48 A20 20 0 0 0 52 28 Z" fill="none" stroke="var(--gold-soft)" stroke-width="3"/>
  <rect x="55" y="55" width="335" height="450" fill="none" stroke="var(--gold-muted)" stroke-width="0.8"/>
  <text class="brand" x="223" y="222" text-anchor="middle" font-size="44" fill="var(--gold-soft)">Bar Pemberly</text>
  <text class="desc" x="223" y="247" text-anchor="middle" font-size="13" fill="var(--gold-soft)">A Speakeasy Experience</text>
  <rect role="img" aria-label="ornamental flourish" x="183" y="310" width="80" height="16" rx="8" fill="var(--gold-soft)" opacity="0.35"/>
  <line x1="122" y1="428" x2="325" y2="428" stroke="var(--gold-soft)" stroke-width="1"/>
  <circle cx="122" cy="428" r="2" fill="var(--gold-soft)"/><circle cx="325" cy="428" r="2" fill="var(--gold-soft)"/>
  <g class="desc" font-size="10" fill="var(--gold-soft)" text-anchor="middle">
    <text x="223" y="447">Discover the allure of a bygone era at Bar</text>
    <text x="223" y="465">Pemberly, where exquisite concoctions and</text>
    <text x="223" y="483">timeless elegance converge.</text>
  </g>
</svg>

<!-- Smoky Maple Sour -->
<svg class="page col-1 row-1" viewBox="0 0 397 497">
  <rect width="397" height="497" fill="var(--charcoal)"/>
  <g fill="none" stroke="var(--gold-muted)" stroke-width="2">
    <rect x="24" y="26" width="349" height="445"/>
    <rect x="32" y="34" width="12" height="12"/><rect x="353" y="34" width="12" height="12"/>
    <rect x="32" y="451" width="12" height="12"/><rect x="353" y="451" width="12" height="12"/>
    <rect x="44" y="46" width="309" height="405" stroke-width="0"/>
  </g>
  <text class="brand" x="198" y="74" text-anchor="middle" font-size="20" fill="var(--gold-muted)">Bar Pemberly</text>
  <rect role="img" aria-label="ornamental flourish" x="163" y="92" width="70" height="14" rx="7" fill="var(--gold-muted)" opacity="0.4"/>
  <text class="title-cookie" x="198" y="147" text-anchor="middle" font-size="36" fill="var(--gold-muted)">Smoky Maple Sour</text>
  <rect role="img" aria-label="ornamental flourish" x="163" y="168" width="70" height="14" rx="7" fill="var(--gold-muted)" opacity="0.4"/>
  <g fill="none" stroke="var(--gold-muted)" stroke-width="1.5">
    <rect x="166" y="200" width="170" height="176"/><rect x="171" y="205" width="160" height="166" stroke-width="0.8"/>
  </g>
  <rect role="img" aria-label="Photo of a bourbon cocktail being strained over ice" x="176" y="210" width="150" height="156" fill="url(#photo-tone)"/>
  <g fill="var(--charcoal)" stroke="var(--gold-muted)" stroke-width="1.5">
    <rect x="60" y="216" width="140" height="152"/>
  </g>
  <rect x="65" y="221" width="130" height="142" fill="none" stroke="var(--gold-muted)" stroke-width="0.8"/>
  <rect role="img" aria-label="Photo of a gin cocktail with orange and cinnamon" x="71" y="227" width="118" height="130" fill="url(#photo-tone)"/>
  <g class="desc" font-size="10" fill="var(--gold-muted)" text-anchor="middle">
    <text x="198" y="403">Rich bourbon, infused with smoky maple syrup and a squeeze of</text>
    <text x="198" y="419">fresh lemon. A modern twist on a classic favorite.</text>
  </g>
  <rect role="img" aria-label="ornamental flourish" x="170" y="434" width="56" height="12" rx="6" fill="var(--gold-muted)" opacity="0.4"/>
</svg>

<!-- Secret Garden -->
<svg class="page col-2 row-1" viewBox="0 0 397 497">
  <rect width="397" height="497" fill="var(--charcoal)"/>
  <path d="M48 28 H350 A20 20 0 0 0 370 48 V452 A20 20 0 0 0 350 472 H48 A20 20 0 0 0 28 452 V48 A20 20 0 0 0 48 28 Z" fill="none" stroke="var(--gold-muted)" stroke-width="2.5"/>
  <rect x="40" y="40" width="318" height="420" fill="none" stroke="var(--gold-muted)" stroke-width="0.8" stroke-dasharray="1.5 2.5"/>
  <text class="brand" x="198" y="74" text-anchor="middle" font-size="20" fill="var(--gold-muted)">Bar Pemberly</text>
  <text class="title-script" x="198" y="138" text-anchor="middle" font-size="54" fill="var(--gold-muted)">Secret Garden</text>
  <line x1="78" y1="180" x2="165" y2="180" stroke="var(--gold-muted)"/><line x1="232" y1="180" x2="320" y2="180" stroke="var(--gold-muted)"/>
  <rect role="img" aria-label="ornamental flourish" x="170" y="173" width="58" height="14" rx="7" fill="var(--gold-muted)" opacity="0.4"/>
  <g class="desc" font-size="10" fill="var(--gold-muted)" text-anchor="middle">
    <text x="198" y="209">A refreshing medley of gin, elderflower, mint, and</text>
    <text x="198" y="225">cucumber. A whisper of summer's kiss in every sip</text>
  </g>
  <g fill="none" stroke="var(--gold-muted)">
    <rect x="55" y="240" width="136" height="172" stroke-width="2"/><rect x="59" y="244" width="128" height="164" stroke-width="0.8"/>
    <rect x="207" y="240" width="136" height="172" stroke-width="2"/><rect x="211" y="244" width="128" height="164" stroke-width="0.8"/>
  </g>
  <line x1="78" y1="436" x2="165" y2="436" stroke="var(--gold-muted)"/><line x1="232" y1="436" x2="320" y2="436" stroke="var(--gold-muted)"/>
  <rect role="img" aria-label="ornamental flourish" x="170" y="429" width="58" height="14" rx="7" fill="var(--gold-muted)" opacity="0.4"/>
</svg>

<!-- Crimson Temptation -->
<svg class="page col-3 row-1" viewBox="0 0 397 497">
  <rect width="397" height="497" fill="var(--charcoal)"/>
  <g fill="none" stroke="var(--gold-muted)">
    <rect x="20" y="22" width="357" height="452" stroke-width="2.5"/>
    <rect x="28" y="30" width="341" height="436" stroke-width="1.2"/>
  </g>
  <text class="brand" x="198" y="74" text-anchor="middle" font-size="20" fill="var(--gold-muted)">Bar Pemberly</text>
  <g class="title-swash" font-size="28" fill="var(--gold-soft)" text-anchor="middle">
    <text x="198" y="116">Crimson</text>
    <text x="198" y="151">Temptation</text>
  </g>
  <line x1="78" y1="180" x2="165" y2="180" stroke="var(--gold-muted)"/><line x1="232" y1="180" x2="320" y2="180" stroke="var(--gold-muted)"/>
  <rect role="img" aria-label="ornamental flourish" x="170" y="173" width="58" height="14" rx="7" fill="var(--gold-muted)" opacity="0.4"/>
  <g fill="none" stroke="var(--gold-muted)">
    <rect x="48" y="202" width="142" height="180" stroke-width="2"/><rect x="52" y="206" width="134" height="172" stroke-width="0.8"/>
    <rect x="206" y="202" width="144" height="180" stroke-width="2"/><rect x="210" y="206" width="136" height="172" stroke-width="0.8"/>
  </g>
  <line x1="78" y1="405" x2="165" y2="405" stroke="var(--gold-muted)"/><line x1="232" y1="405" x2="320" y2="405" stroke="var(--gold-muted)"/>
  <rect role="img" aria-label="ornamental flourish" x="170" y="398" width="58" height="14" rx="7" fill="var(--gold-muted)" opacity="0.4"/>
  <g class="desc" font-size="10" fill="var(--gold-muted)" text-anchor="middle">
    <text x="198" y="430">Vibrant pomegranate liqueur and citrus vodka dance in</text>
    <text x="198" y="446">harmony, with a splash of cranberry. A sip of seduction.</text>
  </g>
</svg>

<!-- Midnight Martini, layered photos -->
<svg class="page col-1 row-2" viewBox="0 0 397 497">
  <rect width="397" height="497" fill="var(--charcoal)"/>
  <path d="M50 26 H348 A22 22 0 0 0 370 48 V450 A22 22 0 0 0 348 472 H50 A22 22 0 0 0 28 450 V48 A22 22 0 0 0 50 26 Z" fill="none" stroke="var(--gold-soft)" stroke-width="2.5"/>
  <text class="brand" x="198" y="74" text-anchor="middle" font-size="20" fill="var(--gold-soft)">Bar Pemberly</text>
  <g class="title-swash" font-size="30" fill="var(--gold-soft)" text-anchor="middle">
    <text x="198" y="120">Midnight</text>
    <text x="198" y="162">Martini</text>
  </g>
  <line x1="78" y1="199" x2="165" y2="199" stroke="var(--gold-soft)"/><line x1="232" y1="199" x2="320" y2="199" stroke="var(--gold-soft)"/>
  <rect role="img" aria-label="ornamental flourish" x="170" y="192" width="58" height="14" rx="7" fill="var(--gold-soft)" opacity="0.4"/>
  <g class="desc" font-size="10" fill="var(--gold-soft)" text-anchor="middle">
    <text x="198" y="228">Smooth vodka or gin, shaken with vermouth and a twist</text>
    <text x="198" y="244">of lemon. Served in a chilled martini glass.</text>
  </g>
  <g fill="none" stroke="var(--gold-muted)">
    <rect x="98" y="268" width="244" height="160" stroke-width="1.5"/><rect x="103" y="273" width="234" height="150" stroke-width="0.8"/>
  </g>
  <rect role="img" aria-label="Photo of a gin cocktail with orange and cinnamon" x="110" y="280" width="220" height="136" fill="url(#photo-tone)"/>
  <rect x="62" y="312" width="116" height="144" fill="var(--charcoal)" stroke="var(--gold-muted)" stroke-width="1.5"/>
  <rect x="67" y="317" width="106" height="134" fill="none" stroke="var(--gold-muted)" stroke-width="0.8"/>
  <rect role="img" aria-label="Photo of a bourbon cocktail being strained over ice" x="72" y="322" width="96" height="124" fill="url(#photo-tone)"/>
</svg>

<!-- Classic Old Fashioned, single photo -->
<svg class="page col-2 row-2" viewBox="0 0 397 497">
  <rect width="397" height="497" fill="var(--ink)"/>
  <path d="M44 27 H352 A18 18 0 0 0 370 45 V454 A18 18 0 0 0 352 472 H44 A18 18 0 0 0 26 454 V45 A18 18 0 0 0 44 27 Z" fill="none" stroke="var(--gold-bright)" stroke-width="1.5"/>
  <rect x="36" y="37" width="325" height="425" fill="none" stroke="var(--gold-bright)" stroke-width="0.7" stroke-dasharray="1.5 2.5"/>
  <text class="brand" x="198" y="74" text-anchor="middle" font-size="20" fill="var(--gold-bright)">Bar Pemberly</text>
  <text class="brand" x="198" y="124" text-anchor="middle" font-size="34" fill="var(--gold-bright)">The Classic Old Fashioned</text>
  <line x1="66" y1="133" x2="330" y2="133" stroke="var(--gold-bright)"/>
  <rect role="img" aria-label="ornamental flourish" x="175" y="140" width="46" height="12" rx="6" fill="var(--gold-bright)" opacity="0.4"/>
  <line x1="199" y1="195" x2="199" y2="415" stroke="var(--gold-muted)"/>
  <g class="desc" font-size="10" fill="var(--gold-bright)" text-anchor="middle">
    <text x="134" y="279">A blend of bourbon, bitters,</text>
    <text x="134" y="295">and a hint of orange essence,</text>
    <text x="134" y="311">stirred to perfection. Served</text>
    <text x="134" y="327">over a large ice cube.</text>
  </g>
  <rect role="img" aria-label="Photo of a bourbon cocktail being strained over ice" x="215" y="196" width="122" height="194" fill="url(#photo-tone)"/>
  <g fill="var(--gold-bright)" stroke="var(--gold-bright)">
    <path d="M164 448 l3 -3 l3 3 l-3 3 Z"/><path d="M178 448 l4 -4 l4 4 l-4 4 Z" fill="none" stroke-width="1.5"/>
    <path d="M211 448 l4 -4 l4 4 l-4 4 Z" fill="none" stroke-width="1.5"/><path d="M226 448 l3 -3 l3 3 l-3 3 Z"/>
  </g>
</svg>

<!-- Classic Old Fashioned, two photos -->
<svg class="page col-3 row-2" viewBox="0 0 397 497">
  <rect width="397" height="497" fill="var(--ink)"/>
  <path d="M44 27 H352 A18 18 0 0 0 370 45 V454 A18 18 0 0 0 352 472 H44 A18 18 0 0 0 26 454 V45 A18 18 0 0 0 44 27 Z" fill="none" stroke="var(--gold-bright)" stroke-width="1.5"/>
  <rect x="36" y="37" width="325" height="425" fill="none" stroke="var(--gold-bright)" stroke-width="0.7" stroke-dasharray="1.5 2.5"/>
  <text class="brand" x="198" y="74" text-anchor="middle" font-size="20" fill="var(--gold-bright)">Bar Pemberly</text>
  <text class="brand" x="198" y="124" text-anchor="middle" font-size="34" fill="var(--gold-bright)">The Classic Old Fashioned</text>
  <line x1="66" y1="133" x2="330" y2="133" stroke="var(--gold-bright)"/>
  <rect role="img" aria-label="ornamental flourish" x="175" y="140" width="46" height="12" rx="6" fill="var(--gold-bright)" opacity="0.4"/>
  <rect role="img" aria-label="Photo of a bourbon cocktail being strained over ice" x="60" y="180" width="122" height="168" fill="url(#photo-tone)"/>
  <line x1="199" y1="180" x2="199" y2="348" stroke="var(--gold-muted)"/>
  <rect role="img" aria-label="Photo of a gin cocktail with orange and cinnamon" x="216" y="180" width="122" height="168" fill="url(#photo-tone)"/>
  <g class="desc" font-size="10" fill="var(--gold-bright)" text-anchor="middle">
    <text x="198" y="393">A blend of bourbon, bitters, and a hint of orange essence,</text>
    <text x="198" y="409">stirred to perfection. Served over a large ice cube.</text>
  </g>
  <g fill="var(--gold-bright)" stroke="var(--gold-bright)">
    <path d="M164 448 l3 -3 l3 3 l-3 3 Z"/><path d="M178 448 l4 -4 l4 4 l-4 4 Z" fill="none" stroke-width="1.5"/>
    <path d="M211 448 l4 -4 l4 4 l-4 4 Z" fill="none" stroke-width="1.5"/><path d="M226 448 l3 -3 l3 3 l-3 3 Z"/>
  </g>
</svg>

<!-- Midnight Martini, single wide photo -->
<svg class="page col-1 row-3" viewBox="0 0 397 497">
  <rect width="397" height="497" fill="var(--charcoal)"/>
  <path d="M50 26 H348 A22 22 0 0 0 370 48 V450 A22 22 0 0 0 348 472 H50 A22 22 0 0 0 28 450 V48 A22 22 0 0 0 50 26 Z" fill="none" stroke="var(--gold-soft)" stroke-width="2.5"/>
  <text class="brand" x="198" y="74" text-anchor="middle" font-size="20" fill="var(--gold-soft)">Bar Pemberly</text>
  <g class="title-swash" font-size="30" fill="var(--gold-soft)" text-anchor="middle">
    <text x="198" y="128">Midnight</text>
    <text x="198" y="170">Martini</text>
  </g>
  <line x1="78" y1="205" x2="165" y2="205" stroke="var(--gold-soft)"/><line x1="232" y1="205" x2="320" y2="205" stroke="var(--gold-soft)"/>
  <rect role="img" aria-label="ornamental flourish" x="170" y="198" width="58" height="14" rx="7" fill="var(--gold-soft)" opacity="0.4"/>
  <g class="desc" font-size="10" fill="var(--gold-soft)" text-anchor="middle">
    <text x="198" y="233">Smooth vodka or gin, shaken with vermouth and a twist</text>
    <text x="198" y="249">of lemon. Served in a chilled martini glass.</text>
  </g>
  <g fill="none" stroke="var(--gold-muted)">
    <rect x="75" y="290" width="247" height="162" stroke-width="1.5"/><rect x="80" y="295" width="237" height="152" stroke-width="0.8"/>
  </g>
  <rect role="img" aria-label="Photo of a gin cocktail with orange and cinnamon" x="90" y="302" width="218" height="136" fill="url(#photo-tone)"/>
</svg>

<!-- Enchanted Elixir -->
<svg class="page col-2 row-3" viewBox="0 0 397 497">
  <rect width="397" height="497" fill="var(--charcoal)"/>
  <g fill="none" stroke="var(--gold-muted)" stroke-width="2">
    <rect x="24" y="26" width="349" height="445"/>
    <rect x="32" y="34" width="12" height="12"/><rect x="353" y="34" width="12" height="12"/>
    <rect x="32" y="451" width="12" height="12"/><rect x="353" y="451" width="12" height="12"/>
  </g>
  <text class="brand" x="198" y="74" text-anchor="middle" font-size="20" fill="var(--gold-muted)">Bar Pemberly</text>
  <text class="title-script" x="198" y="132" text-anchor="middle" font-size="46" fill="var(--gold-muted)">Enchanted Elixir</text>
  <rect role="img" aria-label="ornamental flourish" x="168" y="146" width="62" height="16" rx="8" fill="var(--gold-muted)" opacity="0.4"/>
  <g fill="none" stroke="var(--gold-muted)">
    <path d="M70 187 H175 L206 269 L175 351 H70 L39 269 Z" stroke-width="2"/>
    <path d="M74 193 H171 L200 269 L171 345 H74 L45 269 Z" stroke-width="0.8"/>
    <path d="M222 187 H327 L358 269 L327 351 H222 L191 269 Z" stroke-width="2"/>
    <path d="M226 193 H323 L352 269 L323 345 H226 L197 269 Z" stroke-width="0.8"/>
  </g>
  <g class="desc" font-size="10" fill="var(--gold-muted)" text-anchor="middle">
    <text x="198" y="404">Rich bourbon, infused with smoky maple syrup and a squeeze of</text>
    <text x="198" y="420">fresh lemon. A modern twist on a classic favorite.</text>
  </g>
  <rect role="img" aria-label="ornamental flourish" x="170" y="434" width="56" height="12" rx="6" fill="var(--gold-muted)" opacity="0.4"/>
</svg>

<!-- Whiskey Barrel Mule -->
<svg class="page col-3 row-3" viewBox="0 0 397 497">
  <rect width="397" height="497" fill="var(--ink)"/>
  <g fill="none" stroke="var(--gold-muted)" stroke-width="2">
    <rect x="24" y="26" width="349" height="445"/>
    <rect x="32" y="34" width="12" height="12"/><rect x="353" y="34" width="12" height="12"/>
    <rect x="32" y="451" width="12" height="12"/><rect x="353" y="451" width="12" height="12"/>
  </g>
  <text class="brand" x="198" y="74" text-anchor="middle" font-size="20" fill="var(--gold-bright)">Bar Pemberly</text>
  <text class="brand" x="198" y="131" text-anchor="middle" font-size="34" fill="var(--gold-bright)">Whiskey Barrel Mule</text>
  <line x1="75" y1="140" x2="330" y2="140" stroke="var(--gold-bright)"/>
  <rect role="img" aria-label="ornamental flourish" x="175" y="147" width="46" height="12" rx="6" fill="var(--gold-bright)" opacity="0.4"/>
  <g class="desc" font-size="10" fill="var(--gold-bright)" text-anchor="middle">
    <text x="198" y="196">A blend of whiskey, ginger beer, and lime, aged in oak for</text>
    <text x="198" y="212">a hint of smokiness. Served over ice with a lime wedge.</text>
  </g>
  <g fill="none" stroke="var(--gold-bright)">
    <ellipse cx="130" cy="338" rx="62" ry="88" stroke-width="1.8"/><ellipse cx="130" cy="338" rx="56" ry="82" stroke-width="0.8"/>
    <ellipse cx="268" cy="338" rx="62" ry="88" stroke-width="1.8"/><ellipse cx="268" cy="338" rx="56" ry="82" stroke-width="0.8"/>
  </g>
  <rect role="img" aria-label="ornamental flourish" x="112" y="240" width="36" height="10" rx="5" fill="var(--gold-bright)" opacity="0.4"/>
  <rect role="img" aria-label="ornamental flourish" x="250" y="240" width="36" height="10" rx="5" fill="var(--gold-bright)" opacity="0.4"/>
  <rect role="img" aria-label="ornamental flourish" x="112" y="426" width="36" height="10" rx="5" fill="var(--gold-bright)" opacity="0.4"/>
  <rect role="img" aria-label="ornamental flourish" x="250" y="426" width="36" height="10" rx="5" fill="var(--gold-bright)" opacity="0.4"/>
  <line x1="68" y1="455" x2="160" y2="455" stroke="var(--gold-muted)"/><line x1="236" y1="455" x2="330" y2="455" stroke="var(--gold-muted)"/>
  <g fill="var(--gold-bright)" stroke="var(--gold-bright)">
    <path d="M164 455 l3 -3 l3 3 l-3 3 Z"/><path d="M178 455 l4 -4 l4 4 l-4 4 Z" fill="none" stroke-width="1.5"/>
    <path d="M211 455 l4 -4 l4 4 l-4 4 Z" fill="none" stroke-width="1.5"/><path d="M226 455 l3 -3 l3 3 l-3 3 Z"/>
  </g>
</svg>

</body>
</html>
```